Building Referrer Relationships Booklet

4 page A4 booklet to give to potential professional referrers to establish a collaborative relationship.Needs to be bright, vibrant, colourful, friendly, inviting, in keeping with The Stride Studio colours.
Want to provide potential referrer partners a great reason to choose to collaborate with us. They need to know who we are, what makes us different/appealing, and who we are looking for to connect with.
The final product should communicate high performance and connectedness.

Target Market(s)

professional medical allied health and fitness practitioners

Industry/Entity Type

Health

Requirements
Must have
• energetic, vibrant, engaging, inviting, images

```html
<!DOCTYPE html>
<html lang="en">
<head>
<meta charset="utf-8">
<title>The Stride Studio – Referral Partnerships Booklet</title>
<link href="https://fonts.googleapis.com/css2?family=Montserrat:wght@400;600;700;800&family=Open+Sans:ital,wght@0,400;0,600;0,700;1,400&display=swap" rel="stylesheet">
<style>
  :root{
    --blue:#1c5fa8;
    --blue-dark:#164d8c;
    --blue-soft:#6a97cc;
    --orange:#f26b22;
    --ink:#2b2b2b;
    --muted:#555;
    --paper:#ffffff;
    --bg:#ddd6d1;
  }
  *{box-sizing:border-box;margin:0;padding:0}
  html,body{width:880px;height:1200px;overflow:hidden;background:var(--bg)}
  body{font-family:"Open Sans",Arial,sans-serif;color:var(--ink);position:relative}
  .spread{position:absolute;left:40px;width:800px;height:566px;display:flex;box-shadow:0 6px 18px rgba(0,0,0,.18)}
  .spread--outer{top:22px}
  .spread--inner{top:612px}
  .page{position:relative;width:400px;height:566px;background:var(--paper);overflow:hidden}
  .page + .page{border-left:1px solid #e6e6e6}
  .abs{position:absolute}
  .photo{position:absolute}
  h2,h3,.display{font-family:"Montserrat",Arial,sans-serif}

  /* back cover */
  .runner-photo{left:0;top:0;width:150px;height:470px;background:linear-gradient(180deg,#7fa9d8 0%,#3c6aa6 40%,#2f8a6a 70%,#5f7fb0 100%)}
  .partners-panel{left:150px;top:0;width:250px;height:470px;background:var(--blue);padding:30px 18px 10px 18px;color:#fff}
  .partners-panel h2{color:var(--orange);font-size:17px;font-weight:700;line-height:1.1;margin-bottom:12px;text-transform:uppercase}
  .tick-list{list-style:none}
  .tick-list li{position:relative;padding-left:18px;margin-bottom:7px;font-size:7.2px;line-height:1.3}
  .tick-list li strong{display:block;font-size:7.8px}
  .tick-list svg{position:absolute;left:0;top:1px;width:11px;height:11px}
  .contact{left:22px;bottom:20px;font-family:"Montserrat",Arial,sans-serif}
  .contact .label{font-weight:700;font-size:11px;margin-bottom:3px}
  .contact p{font-size:11px;display:flex;align-items:center;gap:5px;line-height:1.35}
  .contact svg{width:10px;height:10px}
  .badges{right:22px;bottom:30px;width:170px;display:flex;flex-wrap:wrap;gap:10px 14px;justify-content:flex-end}
  .badge{width:30px;height:14px;background:#c9d3df}
  .badge--round{width:16px;height:16px;border-radius:50%;background:#e7c9a2}
  .badge--red{background:#e3a6a6}

  /* front cover */
  .brand{left:0;width:400px;top:26px;text-align:center;font-family:"Montserrat",Arial,sans-serif}
  .brand-mark{width:34px;height:34px;border-radius:50%;background:var(--blue);margin:0 auto 4px}
  .brand-name{font-size:10px;font-weight:700;color:var(--blue)}
  .cover-title{left:0;width:400px;top:96px;text-align:center}
  .cover-title .line1{font-size:15px;font-weight:400;color:var(--blue);letter-spacing:.5px}
  .cover-title .line2{font-size:15px;font-weight:800;color:var(--orange);letter-spacing:.2px}
  .jump-photo{left:0;top:148px;width:400px;height:228px;background:linear-gradient(180deg,#4d9be0 0%,#8fc4ee 45%,#6fa04a 75%,#4c7a2c 100%)}
  .cover-tagline{left:0;width:400px;top:404px;text-align:center;font-family:"Montserrat",Arial,sans-serif;font-size:13px;letter-spacing:.6px;color:var(--ink);line-height:1.35}
  .web-pill{left:125px;top:452px;width:150px;height:20px;border-radius:10px;background:var(--orange);color:#fff;font-size:9px;font-weight:600;text-align:center;line-height:20px}

  /* inner left */
  .about{left:26px;top:22px;width:350px}
  .about h3{color:var(--blue-soft);font-size:9px;font-weight:600;margin-bottom:6px}
  .values{font-family:"Montserrat",Arial,sans-serif;font-size:7.5px;font-weight:700;margin-bottom:6px}
  .about p{font-size:6.6px;line-height:1.45;color:var(--muted);margin-bottom:6px}
  .passion{left:26px;top:140px;width:350px;color:var(--blue-soft);font-family:"Montserrat",Arial,sans-serif;font-size:9.5px;font-style:italic;line-height:1.3;text-transform:uppercase}
  .anatomy-photo{left:26px;top:178px;width:150px;height:110px;background:radial-gradient(ellipse at 55% 50%,#b5483a 0%,#6d2a22 45%,#0d0d0d 80%)}
  .top-three{left:190px;top:182px;width:190px}
  .top-three h3{font-size:8px;font-weight:700;margin-bottom:5px;line-height:1.3}
  .top-three p{font-size:6.8px;line-height:1.45;color:var(--muted)}
  .team-panel{left:0;top:360px;width:270px;height:150px;background:var(--blue-soft);padding:16px 24px;color:#fff}
  .team-panel h3{font-size:9px;font-weight:600;margin-bottom:6px;text-transform:uppercase}
  .team-panel .tick-list li{font-size:6.6px;margin-bottom:3px;padding-left:14px;text-transform:uppercase}
  .team-panel .tick-list svg{width:9px;height:9px}
  .scan-photo{left:270px;top:360px;width:130px;height:206px;background:linear-gradient(160deg,#e8e8e8 0%,#9aa4ae 50%,#2e3a47 100%)}
  .inner-contact{left:26px;bottom:16px;font-family:"Montserrat",Arial,sans-serif}
  .inner-contact p{font-size:10.5px;display:flex;align-items:center;gap:5px;line-height:1.4}
  .inner-contact svg{width:10px;height:10px}

  /* inner right */
  .athletes-photo{left:0;top:0;width:400px;height:190px;background:linear-gradient(180deg,#6fa3d4 0%,#4f7fb6 35%,#3b8f5e 65%,#2c6f9e 100%)}
  .way{left:18px;top:202px;width:250px}
  .way h3{color:var(--blue-soft);font-size:10px;font-weight:600;margin-bottom:3px}
  .way .lead{font-size:7px;font-weight:700;line-height:1.35;margin-bottom:5px}
  .way h4{color:var(--blue-soft);font-family:"Montserrat",Arial,sans-serif;font-size:8px;font-weight:600;margin-bottom:4px}
  .way .tick-list li{font-size:6.2px;color:var(--muted);padding-left:13px;margin-bottom:4px}
  .way .tick-list li strong{display:inline;font-size:6.4px;color:var(--ink)}
  .way .tick-list svg{width:9px;height:9px}
  .achievements{left:278px;top:236px;width:106px;height:174px;background:var(--blue-soft);color:#fff;padding:10px 8px}
  .achievements h3{font-size:8px;font-weight:700;margin-bottom:6px;line-height:1.2}
  .achievements .tick-list li{font-size:6px;padding-left:11px;margin-bottom:4px}
  .achievements .tick-list svg{width:8px;height:8px}
  .foot-photo{left:0;top:370px;width:200px;height:196px;background:linear-gradient(150deg,#f2d6c2 0%,#d9a98c 50%,#c9c9c9 100%)}
  .foot-line{left:70px;top:420px;width:2px;height:120px;background:#e32020;transform:rotate(-35deg)}
  .biohack{left:212px;top:420px;width:176px}
  .biohack h3{color:var(--blue-soft);font-size:10px;font-weight:600;margin-bottom:5px}
  .biohack p{font-size:6.4px;line-height:1.45;color:var(--muted);margin-bottom:4px}
  .biohack p strong{color:var(--ink)}
</style>
</head>
<body>
<svg width="0" height="0" style="position:absolute" aria-hidden="true">
  <symbol id="tick" viewBox="0 0 12 12">
    <circle cx="6" cy="6" r="5.2" fill="none" stroke="currentColor" stroke-width="1"/>
    <path d="M3.4 6.2l1.8 1.8 3.6-3.8" fill="none" stroke="currentColor" stroke-width="1.2"/>
  </symbol>
  <symbol id="phone" viewBox="0 0 12 12">
    <path d="M3 1l2 2.5-1.2 1.3a7 7 0 0 0 3.4 3.4L8.5 7 11 9l-1.3 1.8C5.5 11 1 6.5 1.2 2.3z" fill="currentColor"/>
  </symbol>
  <symbol id="globe" viewBox="0 0 12 12">
    <circle cx="6" cy="6" r="5" fill="none" stroke="currentColor" stroke-width="1"/>
    <ellipse cx="6" cy="6" rx="2.2" ry="5" fill="none" stroke="currentColor" stroke-width=".8"/>
    <path d="M1 6h10M2 3.5h8M2 8.5h8" stroke="currentColor" stroke-width=".7"/>
  </symbol>
</svg>

<!-- Outer spread: back cover + front cover -->
<section class="spread spread--outer">
  <article class="page page--back">
    <div class="photo runner-photo" role="img" aria-label="Photo of a sprinter in green and gold running on an athletics track"></div>
    <div class="abs partners-panel">
      <h2>Referral<br>partners required:</h2>
      <ul class="tick-list">
        <li><svg><use href="#tick"/></svg><strong>Massage therapists</strong>Deep tissue and remedial massage therapeutic massage</li>
        <li><svg><use href="#tick"/></svg><strong>Fascial therapists</strong>Fascial lines releases to reset the alignment of the whole body</li>
        <li><svg><use href="#tick"/></svg><strong>Physiotherapists</strong>Pain relief, protect and strengthen both lower limb and upper limb</li>
        <li><svg><use href="#tick"/></svg><strong>GP, Sports Physicians</strong>General health, diagnostics, treatment support, prescription medications, specialist referrals</li>
        <li><svg><use href="#tick"/></svg><strong>Osteopaths and chiropractors</strong>Mobilisation and manipulative therapy for the spinal column and limbs</li>
        <li><svg><use href="#tick"/></svg><strong>Dietician and nutritionists</strong>DEXA scan for bone density/lean mass/fat mass. Optimising gut health and nutrition - you are what you eat!</li>
        <li><svg><use href="#tick"/></svg><strong>Psychologists/psychiatrists</strong>Sometimes our physical body cannot get better until we optimise a healthy mind</li>
        <li><svg><use href="#tick"/></svg><strong>Personal trainers, Pilates and yoga instructors</strong>Create awesome body strength, flexibility and resilience</li>
        <li><svg><use href="#tick"/></svg><strong>Surgeons</strong>When conservative methods are ineffective, surgical intervention works well.</li>
      </ul>
    </div>
    <div class="abs contact">
      <p class="label">CONTACT US:</p>
      <p><svg><use href="#phone"/></svg>95550123</p>
      <p><svg><use href="#globe"/></svg>www.thestridestudio.com</p>
    </div>
    <div class="abs badges" aria-label="Partner and accreditation badges">
      <span class="badge"></span><span class="badge"></span><span class="badge"></span><span class="badge--round badge"></span>
      <span class="badge badge--red"></span><span class="badge badge--red"></span>
    </div>
  </article>

  <article class="page page--front">
    <div class="abs brand">
      <div class="brand-mark"></div>
      <div class="brand-name">The Stride Studio</div>
    </div>
    <div class="abs cover-title display">
      <p class="line1">REFERRAL PARTNERSHIPS</p>
      <p class="line2">BECAUSE TOGETHER WE ACHIEVE MORE</p>
    </div>
    <div class="photo jump-photo" role="img" aria-label="Photo of four people jumping joyfully on a green hilltop under a blue sky"></div>
    <p class="abs cover-tagline">WE ARE HERE TO HELP OUR<br>CLIENTS GET BACK ON THEIR FEET</p>
    <div class="abs web-pill">www.thestridestudio.com</div>
  </article>
</section>

<!-- Inner spread -->
<section class="spread spread--inner">
  <article class="page page--about">
    <div class="abs about">
      <h3>ABOUT US:</h3>
      <p class="values">COURAGE | INSPIRATION | FUN | CREATIVE | WOW TEAM</p>
      <p>Courage gives us the strength and confidence to take risks and embrace challenges. Inspiration is our energy, our fuel for success, that life force that feeds us as we grow and develop. Fun generates happiness, and we all function at our best when we are happy.</p>
      <p>Creativity sets us as an innovative leading-edge business. Wow means being the very best we can be and realise our true potential. We are not your average business, our service is not average, and our people are not average. Team and in particular high-performance team means we perform at our very best. Great teamwork creates unity and we accomplish much more than each of us alone.</p>
    </div>
    <p class="abs passion">At The Stride Studio, we are passionate about building strong postural foundations, from the feet up</p>
    <div class="photo anatomy-photo" role="img" aria-label="Illustration of foot anatomy showing muscles and tendons"></div>
    <div class="abs top-three">
      <h3>The top 3 things our clients love about us (and hopefully yours will too):</h3>
      <p>1. Positive energy, enthusiasm and outcomes. NPS average score &gt;9 out of 10.<br>
      2. Trusted leader in the practice of podiatric medicine established 1999, elite experience, latest high-tech equipment.<br>
      3. Focus is on strong feet, not just orthotics! Barefoot Training Method, Fascial Lines, Foot Manual Therapies.</p>
    </div>
    <div class="abs team-panel">
      <h3>Our team:</h3>
      <ul class="tick-list">
        <li><svg><use href="#tick"/></svg>Dr Marcus Pellow (Principal Podiatrist)</li>
        <li><svg><use href="#tick"/></svg>Dr Jenna Colvin (Senior Podiatrist)</li>
        <li><svg><use href="#tick"/></svg>Dr Clara Whitby (Podiatrist)</li>
        <li><svg><use href="#tick"/></svg>Dr Felix Tran (Podiatrist)</li>
        <li><svg><use href="#tick"/></svg>Dana Holloway (Practice Manager)</li>
        <li><svg><use href="#tick"/></svg>Rosa Kettering (Front Office Administrator)</li>
      </ul>
    </div>
    <div class="photo scan-photo" role="img" aria-label="Photo of a clinician reviewing foot X-ray images on computer screens"></div>
    <div class="abs inner-contact">
      <p><svg><use href="#phone"/></svg>95550123</p>
      <p><svg><use href="#globe"/></svg>www.thestridestudio.com</p>
    </div>
  </article>

  <article class="page page--method">
    <div class="photo athletes-photo" role="img" aria-label="Photo of a team of athletes in national uniforms standing on a running track"></div>
    <div class="abs way">
      <h3>The Stride Studio Way</h3>
      <p class="lead">Our pathway to strengthen postural foundations, to create lasting changes for freedom of movement, and ultimately keep us going well beyond what we thought was possible (updated as research and tech changes).</p>
      <h4>Fix Your Feet</h4>
      <ul class="tick-list">
        <li><svg><use href="#tick"/></svg><strong>Fix</strong> the pain. Provide analgesia, reduce inflammation, corn/callus/foreign body removal, ingrown/thickened toenail repair and maintenance, surgery</li>
        <li><svg><use href="#tick"/></svg><strong>Protect</strong> the feet (reduce damage, optimise stability, promote healing). Reduce tissue damage, optimise foot posture, activate neuromuscular/reflexive balance stability, promote tissue repair/cellular regeneration</li>
        <li><svg><use href="#tick"/></svg><strong>Strengthen</strong> the feet (increase strength and resilience). Strengthen intrinsics, connect foot strength to core strength, stimulate neuromuscular strength</li>
      </ul>
    </div>
    <div class="abs achievements">
      <h3>Our Team Achievements:</h3>
      <ul class="tick-list">
        <li><svg><use href="#tick"/></svg>Director, Sports Medicine Council</li>
        <li><svg><use href="#tick"/></svg>Director, Regional Academy of Podiatric Sports Medicine</li>
        <li><svg><use href="#tick"/></svg>External Advisor, State University Podiatric Medical Unit</li>
        <li><svg><use href="#tick"/></svg>Level 1 Barefoot Rehabilitation Instructor</li>
        <li><svg><use href="#tick"/></svg>Foot Manual Therapies trained</li>
        <li><svg><use href="#tick"/></svg>Fascial Lines trained</li>
        <li><svg><use href="#tick"/></svg>Class 3b Laser certified</li>
      </ul>
    </div>
    <div class="photo foot-photo" role="img" aria-label="Photo of a bare foot on a treadmill with a red alignment line"></div>
    <div class="abs biohack">
      <h3>Biohack Your Body</h3>
      <p><strong>4. Protect</strong> the whole body (stability). Optimise postural alignment, activate neuromuscular/reflexive balance stability, customised corrective exercises, improve cellular regeneration, optimise nutrition/healthy gut, optimise healthy mind.</p>
      <p><strong>5. Strengthen</strong> the whole body (strength, elasticity). Strengthen the deep core (stabilisers), increase fascial elasticity/strength, increase functional strength, increase endurance, customised nutrition for specific performance, improve psychological resilience.</p>
      <p><strong>6. Repeat</strong> consistently</p>
    </div>
  </article>
</section>
</body>
</html>
```